Party planning business card design

Revels with Kit is a party planning business

Function Planning: Weddings/Themed Parties/Children's Parties

Adult and Children's Photo Booths
Party Themed boxes,
We can find the venue, entertainment. face painters.

Children's costumes and accessories - Sell / Hire

Web: www.revelswithkit.example
Facebook: Revels with Kit

Industry/Entity Type

Party Planning

Contact Information for Business Card

Revels With Kit, Rosalind Trevick,
Creative Director

Colors
e34297
000000

Requirements
Must have
• on my logo are you able to edit the stars to pink?

```html
<!DOCTYPE html>
<html lang="en">
<head>
<meta charset="utf-8">
<title>Revels with Kit – Business Card</title>
<link rel="stylesheet" href="https://fonts.googleapis.com/css2?family=Fira+Sans+Condensed:ital,wght@0,400;0,500;1,400&display=swap">
<style>
  :root {
    --stage: #f4f5f5;
    --pink: #e34297;
    --pink-deep: #cf3a8a;
    --pink-soft: #f08cc0;
    --plum: #3a1029;
    --plum-dark: #1f0d18;
    --white: #ffffff;
    --ink: #000000;
  }
  * { box-sizing: border-box; margin: 0; padding: 0; }
  html, body {
    width: 1200px; height: 741px; overflow: hidden;
    background: var(--stage);
    font-family: "Fira Sans Condensed", "Arial Narrow", sans-serif;
  }
  .sheet { position: relative; width: 1200px; height: 741px; }
  .card {
    position: absolute; top: 262px;
    width: 363px; height: 207px;
    border: 1px solid var(--ink);
    overflow: hidden;
  }
  .card--front {
    left: 164px;
    background: linear-gradient(180deg, var(--pink-deep) 0%, var(--pink) 100%);
  }
  .front__ornament {
    position: absolute; left: 68px; top: 0;
    width: 295px; height: 207px;
    background: radial-gradient(ellipse at 75% 45%, rgba(255,255,255,0.45) 0%, rgba(255,255,255,0.15) 45%, rgba(255,255,255,0) 75%);
  }
  .front__brand {
    position: absolute; left: 34px; top: 140px;
    font-size: 36px; font-weight: 400; color: var(--white);
    letter-spacing: -0.5px; white-space: nowrap;
  }
  .card--back {
    left: 676px;
    background: radial-gradient(ellipse at 0% 40%, var(--plum) 0%, var(--plum-dark) 75%);
  }
  .back__name {
    position: absolute; top: 20px; width: 100%; text-align: center;
    font-size: 18px; font-weight: 400; color: var(--white);
  }
  .back__role {
    position: absolute; top: 44px; width: 100%; text-align: center;
    font-size: 13px; font-style: italic; color: var(--pink-soft);
  }
  .back__rule {
    position: absolute; top: 71px; left: 38px; width: 286px; height: 1px;
    background: linear-gradient(90deg, rgba(227,66,151,0) 0%, var(--pink) 50%, rgba(227,66,151,0) 100%);
  }
  .contact { position: absolute; left: 102px; top: 100px; list-style: none; }
  .contact__item {
    display: flex; align-items: center; height: 25px;
    font-size: 14px; font-style: italic; color: var(--white);
  }
  .contact__icon { width: 12px; height: 12px; margin-right: 12px; fill: var(--white); }
</style>
</head>
<body>
<main class="sheet">
  <section class="card card--front" aria-label="Card front">
    <div class="front__ornament" role="img" aria-label="White floral swirl ornament with scattered petals"></div>
    <p class="front__brand">Revels with Kit</p>
  </section>

  <section class="card card--back" aria-label="Card back">
    <h1 class="back__name">Rosalind Trevick</h1>
    <p class="back__role">Creative Director</p>
    <div class="back__rule"></div>
    <ul class="contact">
      <li class="contact__item">
        <svg class="contact__icon" viewBox="0 0 12 12" aria-hidden="true"><path d="M2.5 0.5 L4.5 3 L3.5 4.3 Q4.8 7 7.7 8.5 L9 7.5 L11.5 9.5 L10 11.5 Q5 11 0.5 2 Z"/></svg>
        (04) 5550 1927
      </li>
      <li class="contact__item">
        <svg class="contact__icon" viewBox="0 0 12 12" aria-hidden="true"><path d="M0.5 2.5 H11.5 V9.5 H0.5 Z M1.2 3 L6 6.8 L10.8 3" fill="none" stroke="#fff" stroke-width="1"/><path d="M0.5 2.5 H11.5 L6 6.5 Z"/></svg>
        Rosalind@revelswithkit.example
      </li>
      <li class="contact__item">
        <svg class="contact__icon" viewBox="0 0 12 12" aria-hidden="true" fill="none" stroke="#fff" stroke-width="0.9"><circle cx="6" cy="6" r="5.2"/><ellipse cx="6" cy="6" rx="2.3" ry="5.2"/><path d="M0.8 6 H11.2 M1.8 3.3 H10.2 M1.8 8.7 H10.2"/></svg>
        www.revelswithkit.example
      </li>
    </ul>
  </section>
</main>
</body>
</html>
```